VORLEN Website Design

We need a website designed for our company VORLEN. We are a luxury lifestyle club that will provide benefits and services for our members. The site should be clean & sleek, preferably using black and white (or darker colors). (example sites: brimvale.example, tusko.example)

Here is a link of a sample page I did using wix. (https://pelmundry4.sitebuild.example/mypage) This can be used to get a general idea.

Target Market(s)

Upper Middle Class in the United States

Number of Pages Required

5+ page

Font styles to use
Sans Serif
Other font styles liked:
• Arial (or other similar fonts)

Requirements
Must have
• A clean design that is eye-catching and speaks to our company.
Nice to have
• Ideas for copy.

```html
<!DOCTYPE html>
<html lang="en">
<head>
<meta charset="utf-8">
<title>VORLEN — Luxury Lifestyle Club</title>
<link rel="stylesheet" href="https://fonts.googleapis.com/css2?family=Questrial&display=swap">
<style>
:root{
  --navy:#0f1d52;
  --ink:#2b2b2b;
  --muted:#6d6d6d;
  --rule:#d9d9d9;
  --white:#ffffff;
  --sunset-top:#3a2a12;
  --sunset-mid:#e58a12;
  --sunset-low:#7a4a14;
  --green-dark:#2c3524;
  --green-mid:#55653f;
  --crowd-top:#4a1a10;
  --crowd-low:#0d0604;
  --star:#f2c21b;
}
*{box-sizing:border-box;margin:0;padding:0}
html,body{width:1200px;height:2817px;overflow:hidden}
body{font-family:"Questrial",Arial,sans-serif;color:var(--ink);background:var(--white);position:relative}
a{color:inherit;text-decoration:none}

/* Hero */
.hero{position:absolute;left:0;top:0;width:1200px;height:470px;
  background:linear-gradient(180deg,#5a3a14 0%,var(--sunset-mid) 28%,#f0a030 40%,#b86a1a 55%,var(--sunset-low) 75%,#2a1a0a 100%)}
.hero-photo{position:absolute;inset:0}
.nav{position:absolute;left:250px;top:19px;width:700px;height:37px;background:rgba(255,255,255,.55);display:flex;align-items:center}
.brand{font-size:28px;color:#111;padding-left:8px;letter-spacing:1px;flex:1}
.nav-links{display:flex;height:100%;align-items:center;list-style:none;padding-right:8px}
.nav-links li{font-size:12.5px;color:#111;padding:0 10px;height:100%;display:flex;align-items:center}
.nav-links li.active{background:var(--navy);color:var(--white);padding:0 11px}
.slider-dots{position:absolute;left:247px;top:206px;display:flex;flex-direction:column;gap:7px}
.slider-dots span{width:9px;height:9px;border:1.5px solid #fff;border-radius:50%}
.slider-dots span.on{background:#fff}
.contact-title{position:absolute;top:354px;width:100%;text-align:center;color:#fff;font-size:20px;letter-spacing:.3px}
.contact-band{position:absolute;left:0;top:387px;width:1200px;height:49px;background:rgba(190,190,190,.55)}
.contact-form{position:absolute;left:250px;top:400px;width:700px;display:flex;gap:9px}
.contact-form span{height:25px;background:#fff;font-size:10px;color:#999;padding:6px 5px;flex:1}
.contact-form .send{flex:0 0 84px;background:var(--navy);color:#fff;text-align:center}

/* Headings */
.section-title{position:absolute;width:100%;text-align:center;font-size:30px;color:#333}
.title-rule{position:absolute;left:325px;width:550px;height:1px;background:var(--rule)}
.chev{position:absolute;left:592px;width:16px;height:10px}

/* About */
.about-text{position:absolute;top:576px;width:100%;text-align:center;font-size:10.5px;line-height:15px;color:var(--muted)}
.btn-help{position:absolute;left:505px;top:650px;width:192px;height:33px;background:var(--navy);color:#fff;font-size:13.5px;text-align:center;line-height:33px}

/* Services */
.services{position:absolute;left:0;top:723px;width:1200px;height:428px;
  background:radial-gradient(ellipse at 80% 70%,#6b7a3e 0%,transparent 45%),linear-gradient(180deg,#3a4030 0%,var(--green-mid) 40%,var(--green-dark) 100%)}
.services .section-title{color:#fff;top:22px}
.services .title-rule{background:rgba(255,255,255,.35);top:64px}
.service{position:absolute;width:150px;text-align:center;color:#fff}
.service-icon{width:40px;height:40px;border-radius:50%;background:var(--navy);border:2px solid #fff;margin:0 auto;display:flex;align-items:center;justify-content:center}
.service-name{font-size:12.5px;margin-top:6px}
.service-desc{font-size:8px;line-height:9.5px;margin-top:5px;color:#eee}
.service-btn{display:block;width:98px;height:20px;margin:5px auto 0;background:#fff;color:#222;font-size:9.5px;line-height:20px}

/* Work */
.card{position:absolute;width:225px;height:291px;border:1px solid #d5d5d5;background:#fff}
.card-photo{height:173px;width:100%}
.card-title{height:38px;line-height:38px;text-align:center;font-size:16px;color:var(--navy);border-bottom:1px solid #e2e2e2}
.card-desc{height:50px;padding:7px 10px;font-size:8px;line-height:11px;color:#666;text-align:center}
.card-links{display:flex;border-top:1px solid #e2e2e2;height:28px}
.card-links span{flex:1;text-align:center;font-size:9.5px;line-height:26px;color:#333}
.card-links span+span{border-left:1px solid #e2e2e2}

/* Testimonial */
.testimonial{position:absolute;left:0;top:2214px;width:1200px;height:301px;
  background:radial-gradient(circle at 50% 20%,#8a5a10 0%,#5a2010 25%,transparent 55%),linear-gradient(180deg,var(--crowd-top) 0%,#2a0d08 55%,var(--crowd-low) 100%)}
.avatar{position:absolute;left:557px;top:29px;width:86px;height:86px;border-radius:50%;background:#6d5a4e;border:3px solid #fff}
.stars{position:absolute;top:127px;width:100%;text-align:center}
.quote{position:absolute;left:300px;top:148px;width:600px;text-align:center;color:#fff;font-style:italic;font-size:11.5px;line-height:15px}
.quote-by{position:absolute;top:201px;width:100%;text-align:center;color:#fff;font-size:11px}
.quote-nav{position:absolute;left:420px;top:254px;width:360px;height:1px;background:rgba(255,255,255,.35)}

/* Footer */
.socials{position:absolute;top:2531px;width:100%;display:flex;justify-content:center;gap:5px}
.socials span{width:19px;height:19px;background:#6b7480;border-radius:2px}
.footer-rule{position:absolute;left:250px;width:700px;height:1px;background:#e4e4e4}
.footer-col{position:absolute;top:2603px;list-style:none}
.footer-col h4{font-weight:normal;font-size:13px;color:var(--navy);margin-bottom:8px}
.footer-col li{font-size:9.5px;color:#444;line-height:21.6px}
.copyright{position:absolute;top:2787px;width:100%;text-align:center;font-size:8.5px;color:#555}
</style>
</head>
<body>

<header class="hero">
  <div class="hero-photo" role="img" aria-label="Sunset over the sea with silhouetted palm trees, a thatched umbrella and a wooden signpost"></div>
  <nav class="nav">
    <div class="brand">VORLEN</div>
    <ul class="nav-links">
      <li class="active">Home</li><li>About Us</li><li>Our Services</li><li>Blog</li><li>Contact Us</li>
    </ul>
  </nav>
  <div class="slider-dots"><span></span><span class="on"></span><span></span><span></span></div>
  <h2 class="contact-title" style="font-weight:normal">We're always here, drop us a line!</h2>
  <div class="contact-band"></div>
  <form class="contact-form">
    <span>Name</span><span>Email</span><span>Subject</span><span>Message</span><span class="send">Send</span>
  </form>
</header>

<section class="about">
  <h2 class="section-title" style="top:498px;font-weight:normal">About VORLEN</h2>
  <div class="title-rule" style="top:548px"></div>
  <svg class="chev" style="top:541px" viewBox="0 0 16 10"><polyline points="2,2 8,8 14,2" fill="none" stroke="#999" stroke-width="1.5"/></svg>
  <p class="about-text">The ultimate full service lifestyle club<br>VORLEN was formed to bring the best services, experiences, and exclusive opportunities to our members.<br>With everything from private member events to private jet travel, the perks of being a VORLEN member are unmatched.</p>
  <a class="btn-help">How can we help you ?</a>
</section>

<section class="services" role="img" aria-label="Blurred green background of young plants growing from stacked coins">
  <h2 class="section-title" style="font-weight:normal">Our Services</h2>
  <div class="title-rule"></div>
  <svg class="chev" style="top:57px" viewBox="0 0 16 10"><polyline points="2,2 8,8 14,2" fill="none" stroke="#ddd" stroke-width="1.5"/></svg>

  <div class="service" style="left:250px;top:108px"><div class="service-icon"><svg width="18" height="18" viewBox="0 0 18 18"><rect x="2" y="5" width="14" height="10" rx="1" fill="#fff"/><rect x="6" y="2" width="6" height="4" fill="none" stroke="#fff" stroke-width="1.5"/></svg></div><div class="service-name">Accounting Services</div><p class="service-desc">Lorem Ipsum is simply dummy text of the printing and typesetting industry. Lorem Ipsum has been the industry's</p><span class="service-btn">See Our</span></div>
  <div class="service" style="left:432px;top:108px"><div class="service-icon"><svg width="18" height="18" viewBox="0 0 18 18"><rect x="2" y="9" width="10" height="6" fill="#fff"/><circle cx="13" cy="6" r="3" fill="#fff"/></svg></div><div class="service-name">Investment Services</div><p class="service-desc">Lorem Ipsum is simply dummy text of the printing and typesetting industry. Lorem Ipsum has been the industry's</p><span class="service-btn">See Our</span></div>
  <div class="service" style="left:618px;top:108px"><div class="service-icon"><svg width="18" height="18" viewBox="0 0 18 18"><line x1="9" y1="2" x2="9" y2="16" stroke="#fff" stroke-width="1.5"/><line x1="3" y1="5" x2="15" y2="5" stroke="#fff" stroke-width="1.5"/><path d="M1 11 L3 6 L5 11Z M13 11 L15 6 L17 11Z" fill="#fff"/><line x1="5" y1="16" x2="13" y2="16" stroke="#fff" stroke-width="1.5"/></svg></div><div class="service-name">Lawyer Services</div><p class="service-desc">Lorem Ipsum is simply dummy text of the printing and typesetting industry. Lorem Ipsum has been the industry's</p><span class="service-btn">See Our</span></div>
  <div class="service" style="left:800px;top:108px"><div class="service-icon"><svg width="18" height="18" viewBox="0 0 18 18"><path d="M3 9 L9 3 L15 9 V16 H3Z" fill="#fff"/></svg></div><div class="service-name">Real Estate Services</div><p class="service-desc">Lorem Ipsum is simply dummy text of the printing and typesetting industry. Lorem Ipsum has been the industry's</p><span class="service-btn">See Our</span></div>

  <div class="service" style="left:250px;top:266px"><div class="service-icon"><svg width="18" height="18" viewBox="0 0 18 18"><circle cx="6" cy="6" r="3" fill="none" stroke="#fff" stroke-width="1.5"/><circle cx="12" cy="12" r="3" fill="none" stroke="#fff" stroke-width="1.5"/><circle cx="12" cy="5" r="2" fill="#fff"/></svg></div><div class="service-name">Experiences</div><p class="service-desc">Lorem Ipsum is simply dummy text of the printing and typesetting industry. Lorem Ipsum has been the industry's</p><span class="service-btn">See Our</span></div>
  <div class="service" style="left:432px;top:266px"><div class="service-icon"><svg width="18" height="18" viewBox="0 0 18 18"><path d="M9 1 L10.5 7 L17 10 V11.5 L10.5 10 L10 14 L12 16 V17 L9 16 L6 17 V16 L8 14 L7.5 10 L1 11.5 V10 L7.5 7Z" fill="#fff"/></svg></div><div class="service-name">Private Jet Travel</div><p class="service-desc">Lorem Ipsum is simply dummy text of the printing and typesetting industry. Lorem Ipsum has been the industry's</p><span class="service-btn">See Our</span></div>
  <div class="service" style="left:618px;top:266px"><div class="service-icon"><svg width="18" height="18" viewBox="0 0 18 18"><rect x="2" y="4" width="14" height="12" fill="#fff"/><rect x="5" y="2" width="2" height="4" fill="#fff"/><rect x="11" y="2" width="2" height="4" fill="#fff"/></svg></div><div class="service-name">Event Access</div><p class="service-desc">Lorem Ipsum is simply dummy text of the printing and typesetting industry. Lorem Ipsum has been the industry's</p><span class="service-btn">See Our</span></div>
  <div class="service" style="left:800px;top:266px"><div class="service-icon"><svg width="18" height="18" viewBox="0 0 18 18"><rect x="3" y="3" width="12" height="12" fill="#fff"/></svg></div><div class="service-name">Private Events</div><p class="service-desc">Lorem Ipsum is simply dummy text of the printing and typesetting industry. Lorem Ipsum has been the industry's</p><span class="service-btn">See Our</span></div>
</section>

<section class="work">
  <h2 class="section-title" style="top:1189px;font-weight:normal">Recent Work</h2>
  <div class="title-rule" style="top:1240px"></div>
  <svg class="chev" style="top:1233px" viewBox="0 0 16 10"><polyline points="2,2 8,8 14,2" fill="none" stroke="#999" stroke-width="1.5"/></svg>

  <article class="card" style="left:248px;top:1279px"><div class="card-photo" role="img" aria-label="Hands reviewing financial documents with a pen" style="background:linear-gradient(135deg,#5a6a80,#e8ecf0)"></div><h3 class="card-title" style="font-weight:normal">Accounting Services</h3><p class="card-desc">Lorem Ipsum is simply dummy text of the printing and typesetting industry. Lorem Ipsum has been the industry's standard dummy text ever</p><div class="card-links"><span>See Photo</span><span>See Location</span></div></article>
  <article class="card" style="left:486px;top:1279px"><div class="card-photo" role="img" aria-label="Stock market chart on a blue screen" style="background:linear-gradient(135deg,#0b1a3a,#2a4a80)"></div><h3 class="card-title" style="font-weight:normal">Investment Services</h3><p class="card-desc">Lorem Ipsum is simply dummy text of the printing and typesetting industry. Lorem Ipsum has been the industry's standard dummy text ever</p><div class="card-links"><span>See Photo</span><span>See Location</span></div></article>
  <article class="card" style="left:725px;top:1279px"><div class="card-photo" role="img" aria-label="Lawyer in a suit in front of a bookshelf" style="background:linear-gradient(135deg,#6a2a18,#b06a40)"></div><h3 class="card-title" style="font-weight:normal">Lawyer Services</h3><p class="card-desc">Lorem Ipsum is simply dummy text of the printing and typesetting industry. Lorem Ipsum has been the industry's standard dummy text ever</p><div class="card-links"><span>See Photo</span><span>See Location</span></div></article>

  <article class="card" style="left:248px;top:1585px"><div class="card-photo" role="img" aria-label="Happy couple receiving house keys" style="background:linear-gradient(135deg,#2a5a90,#a8c8e0)"></div><h3 class="card-title" style="font-weight:normal">Real Estate Services</h3><p class="card-desc">Lorem Ipsum is simply dummy text of the printing and typesetting industry. Lorem Ipsum has been the industry's standard dummy text ever</p><div class="card-links"><span>See Photo</span><span>See Location</span></div></article>
  <article class="card" style="left:486px;top:1585px"><div class="card-photo" role="img" aria-label="Picture frame on a wooden sideboard in a bright room" style="background:linear-gradient(180deg,#f2efe8,#a08060)"></div><h3 class="card-title" style="font-weight:normal">24/7 Concierge</h3><p class="card-desc">Lorem Ipsum is simply dummy text of the printing and typesetting industry. Lorem Ipsum has been the industry's standard dummy text ever</p><div class="card-links"><span>See Photo</span><span>See Location</span></div></article>
  <article class="card" style="left:725px;top:1585px"><div class="card-photo" role="img" aria-label="Private jet on the tarmac with passengers on a red carpet" style="background:linear-gradient(180deg,#6a9ad0,#c8d8e8 60%,#8a7a6a)"></div><h3 class="card-title" style="font-weight:normal">Private Jet Travel</h3><p class="card-desc">Lorem Ipsum is simply dummy text of the printing and typesetting industry. Lorem Ipsum has been the industry's standard dummy text ever</p><div class="card-links"><span>See Photo</span><span>See Location</span></div></article>

  <article class="card" style="left:248px;top:1891px"><div class="card-photo" role="img" aria-label="Black and white concert stage with spotlights" style="background:radial-gradient(circle at 40% 40%,#d0d0d0,#202020 70%)"></div><h3 class="card-title" style="font-weight:normal">Event Access</h3><p class="card-desc">Lorem Ipsum is simply dummy text of the printing and typesetting industry. Lorem Ipsum has been the industry's standard dummy text ever</p><div class="card-links"><span>See Photo</span><span>See Location</span></div></article>
  <article class="card" style="left:486px;top:1891px"><div class="card-photo" role="img" aria-label="Friends sharing an outdoor dinner party" style="background:linear-gradient(135deg,#4a6a2a,#a06040)"></div><h3 class="card-title" style="font-weight:normal">Private Events</h3><p class="card-desc">Lorem Ipsum is simply dummy text of the printing and typesetting industry. Lorem Ipsum has been the industry's standard dummy text ever</p><div class="card-links"><span>See Photo</span><span>See Location</span></div></article>
  <article class="card" style="left:725px;top:1891px"><div class="card-photo" role="img" aria-label="Diver swimming with a manta ray over a reef" style="background:linear-gradient(180deg,#3ab0d0,#0a4a70)"></div><h3 class="card-title" style="font-weight:normal">Experiences</h3><p class="card-desc">Lorem Ipsum is simply dummy text of the printing and typesetting industry. Lorem Ipsum has been the industry's standard dummy text ever</p><div class="card-links"><span>See Photo</span><span>See Location</span></div></article>
</section>

<section class="testimonial" role="img" aria-label="Silhouetted crowd with raised hands at a sunset concert">
  <div class="avatar" role="img" aria-label="Member portrait"></div>
  <div class="stars"><svg width="70" height="12" viewBox="0 0 70 12"><g fill="#f2c21b"><polygon points="6,0 7.6,4 12,4.4 8.6,7.2 9.7,11.6 6,9.2 2.3,11.6 3.4,7.2 0,4.4 4.4,4"/><polygon transform="translate(14.5 0)" points="6,0 7.6,4 12,4.4 8.6,7.2 9.7,11.6 6,9.2 2.3,11.6 3.4,7.2 0,4.4 4.4,4"/><polygon transform="translate(29 0)" points="6,0 7.6,4 12,4.4 8.6,7.2 9.7,11.6 6,9.2 2.3,11.6 3.4,7.2 0,4.4 4.4,4"/><polygon transform="translate(43.5 0)" points="6,0 7.6,4 12,4.4 8.6,7.2 9.7,11.6 6,9.2 2.3,11.6 3.4,7.2 0,4.4 4.4,4"/><polygon transform="translate(58 0)" points="6,0 7.6,4 12,4.4 8.6,7.2 9.7,11.6 6,9.2 2.3,11.6 3.4,7.2 0,4.4 4.4,4"/></g></svg></div>
  <p class="quote">Lorem Ipsum is simply dummy text of the printing and typesetting industry. Lorem Ipsum has been the industry's standard dummy text ever since the 1500s, when an unknown printer took a galley of type and scrambled it to make a type s survived not only five centuries, but also the leap into</p>
  <p class="quote-by">dario fenwick - 17/Nov/2018</p>
  <div class="quote-nav"></div>
  <svg style="position:absolute;left:588px;top:247px" width="24" height="14" viewBox="0 0 24 14"><circle cx="6" cy="7" r="5.5" fill="#fff"/><circle cx="18" cy="7" r="5.5" fill="#fff"/><polyline points="7.5,4.5 5,7 7.5,9.5" fill="none" stroke="#222" stroke-width="1.3"/><polyline points="16.5,4.5 19,7 16.5,9.5" fill="none" stroke="#222" stroke-width="1.3"/></svg>
</section>

<footer class="site-footer">
  <div class="socials"><span></span><span></span><span></span><span></span><span></span></div>
  <div class="footer-rule" style="top:2567px"></div>
  <ul class="footer-col" style="left:250px"><h4>News &amp; Media</h4><li>Latest Stories</li><li>Press Releases</li><li>Media Inquiries</li><li>Media Partners</li><li>The News</li></ul>
  <ul class="footer-col" style="left:436px"><h4>Support</h4><li>Latest Stories</li><li>Press Releases</li><li>Media Inquiries</li><li>Media Partners</li><li>The News</li></ul>
  <ul class="footer-col" style="left:610px"><h4>Event</h4><li>Latest Stories</li><li>Press Releases</li><li>Media Inquiries</li><li>Media Partners</li><li>The News</li></ul>
  <ul class="footer-col" style="left:768px"><h4>News &amp; Media</h4><li>Submit Your Story</li><li>Member Updates Archive</li><li>Contact</li><li>Login</li></ul>
  <div class="footer-rule" style="top:2766px"></div>
  <p class="copyright">© vorlen.example . 2018. All Rights reserved. &nbsp;Privacy Policy</p>
</footer>

</body>
</html>
```